Business Card Design

We have a group of different function companies owned and operated by one person. We are located in the Dallas Fort Worth area in Texas. We develop properties to where we are owners and develop properties that are not ours as well. We build custom homes and commercial buildings. We also do residential and commercial remodeling. We also own commercial properties in which we lease office space. We are trying to merge all we do into one card and have done so already into one website. We initially had thought of having a logo made with HV in nice attractive lettering maybe as a watermark. We are open to the color scheme but no neons or pastels.

Project Deadline Extended
Reason: I am needing 2 different cards for two businesses.

Industry/Entity Type

Residential

Contact Information for Business Card

Harwell Ventures
4826 Mabry Ln. Suite 417
Alderbrook, Ohio 76109
Land Development
Residential and Commercial Construction
Commercial Real Estate
Dale Wintermoot
www.harwellgrp.example
dale@harwellgrp.example
Cell: 817-555-0142
Office: 817-555-0187
Fax: 8175550163

```html
<!DOCTYPE html>
<html lang="en">
<head>
<meta charset="utf-8">
<title>Harwell Ventures – Business Card</title>
<link rel="stylesheet" href="https://fonts.googleapis.com/css2?family=Pacifico&family=PT+Sans+Narrow:wght@700&family=Montserrat:wght@400;500&display=swap">
<style>
  :root {
    --panel: #141414;
    --ink: #ffffff;
    --ribbon-ink: #1a1a1a;
    --violet: #6a1fe0;
    --blue: #1f4ff0;
    --magenta: #d41cc4;
    --red: #f2301a;
    --orange: #ff8a12;
    --yellow: #f4ee10;
    --lime: #8fe01a;
    --cyan: #38d2e8;
  }
  html, body {
    margin: 0;
    padding: 0;
    width: 1200px;
    height: 702px;
    overflow: hidden;
    background: #ffffff;
  }
  .card {
    position: relative;
    width: 1200px;
    height: 702px;
    overflow: hidden;
    font-family: "Montserrat", sans-serif;
    color: var(--ink);
  }
  .card__backdrop {
    position: absolute;
    inset: 0;
    background:
      radial-gradient(ellipse 45% 50% at 100% 55%, var(--yellow) 0%, rgba(244,238,16,0) 100%),
      radial-gradient(ellipse 40% 35% at 85% 100%, var(--lime) 0%, rgba(143,224,26,0) 100%),
      radial-gradient(ellipse 30% 35% at 55% 100%, var(--cyan) 0%, rgba(56,210,232,0) 100%),
      radial-gradient(ellipse 35% 40% at 8% 40%, var(--magenta) 0%, rgba(212,28,196,0) 100%),
      radial-gradient(ellipse 50% 40% at 60% 0%, var(--red) 0%, rgba(242,48,26,0) 100%),
      linear-gradient(100deg, var(--violet) 0%, var(--blue) 30%, var(--orange) 70%, var(--yellow) 100%);
  }
  .brand-seal {
    position: absolute;
    left: 81px;
    top: 79px;
    width: 75px;
    height: 75px;
    border-radius: 50%;
    background: var(--ink);
    display: flex;
    align-items: center;
    justify-content: center;
    font-family: "Montserrat", sans-serif;
    font-weight: 500;
    font-size: 23px;
    color: var(--ribbon-ink);
  }
  .panel {
    position: absolute;
    left: 160px;
    top: 156px;
    width: 880px;
    height: 389px;
    background: var(--panel);
  }
  .panel__name {
    position: absolute;
    left: 0;
    right: 0;
    top: 4px;
    margin: 0;
    text-align: center;
    font-family: "Pacifico", cursive;
    font-weight: 400;
    font-size: 66px;
    line-height: 1.3;
  }
  .panel__services {
    position: absolute;
    left: 0;
    right: 0;
    top: 124px;
    margin: 0;
    text-align: center;
    font-size: 14.5px;
    letter-spacing: 1.9px;
  }
  .ribbon {
    position: absolute;
    left: 158px;
    top: 159px;
    width: 565px;
    height: 72px;
  }
  .ribbon svg { position: absolute; inset: 0; }
  .ribbon__person {
    position: absolute;
    left: 0;
    right: 0;
    top: 2px;
    margin: 0;
    text-align: center;
    font-family: "PT Sans Narrow", sans-serif;
    font-weight: 700;
    font-size: 41px;
    line-height: 1.1;
    color: var(--ribbon-ink);
  }
  .ribbon__role {
    position: absolute;
    left: 0;
    right: 0;
    top: 46px;
    margin: 0;
    text-align: center;
    font-family: "PT Sans Narrow", sans-serif;
    font-weight: 700;
    font-size: 16px;
    color: var(--ribbon-ink);
  }
  .contact {
    position: absolute;
    display: flex;
    align-items: center;
    gap: 13px;
    font-size: 22px;
    letter-spacing: 3.4px;
    white-space: nowrap;
  }
  .contact__icon {
    width: 25px;
    height: 25px;
    flex: none;
  }
  .contact--address { left: 47px; top: 258px; letter-spacing: 3.1px; }
  .contact--email { left: 47px; top: 308px; font-size: 21px; letter-spacing: 2.3px; }
  .contact--web { left: 486px; top: 308px; font-size: 21px; letter-spacing: 2.2px; gap: 10px; }
  .contact--cell { left: 47px; top: 348px; }
  .contact--office { left: 338px; top: 348px; }
  .contact--fax { left: 610px; top: 348px; }
</style>
</head>
<body>
<main class="card">
  <div class="card__backdrop" role="img" aria-label="Colourful low-poly mosaic of blue, violet, red, orange, yellow, green and cyan facets"></div>

  <div class="brand-seal">HV</div>

  <section class="panel">
    <h1 class="panel__name">Harwell Ventures</h1>
    <p class="panel__services">·Land Development · Residential &amp; Commercial Construction · Commercial Real Estate</p>

    <div class="ribbon">
      <svg viewBox="0 0 565 72" width="565" height="72" aria-hidden="true">
        <polygon points="0,0 565,0 542,36 565,72 0,72 23,36" fill="#ffffff"/>
      </svg>
      <p class="ribbon__person">Dale Wintermoot</p>
      <p class="ribbon__role">President</p>
    </div>

    <div class="contact contact--address">
      <svg class="contact__icon" viewBox="0 0 24 24" aria-hidden="true"><circle cx="12" cy="12" r="12" fill="#fff"/><path d="M12 5.5 5.5 11.5h2v6h3.3v-4h2.4v4h3.3v-6h2z" fill="#141414"/></svg>
      <span>4826 Mabry Ln. Suite 417 Alderbrook, Ohio 76109</span>
    </div>

    <div class="contact contact--email">
      <svg class="contact__icon" viewBox="0 0 24 24" aria-hidden="true"><circle cx="12" cy="12" r="12" fill="#fff"/><rect x="6" y="8" width="12" height="8.5" rx="1" fill="#141414"/><path d="M6.5 8.6 12 12.8l5.5-4.2" fill="none" stroke="#fff" stroke-width="1.1"/></svg>
      <span>dale@harwellgrp.example</span>
    </div>

    <div class="contact contact--web">
      <svg class="contact__icon" viewBox="0 0 24 24" aria-hidden="true"><circle cx="12" cy="12" r="12" fill="#fff"/><path d="M7 12.3l3.2 3.2L17 8.7" fill="none" stroke="#141414" stroke-width="2.4" stroke-linecap="round" stroke-linejoin="round"/></svg>
      <span>www.harwellgrp.example</span>
    </div>

    <div class="contact contact--cell">
      <svg class="contact__icon" viewBox="0 0 24 24" aria-hidden="true"><circle cx="12" cy="12" r="12" fill="#fff"/><rect x="8.5" y="5" width="7" height="14" rx="1.3" fill="#141414"/><rect x="9.6" y="7" width="4.8" height="6" fill="#fff"/><circle cx="12" cy="16.3" r="1" fill="#fff"/></svg>
      <span>817-555-0142</span>
    </div>

    <div class="contact contact--office">
      <svg class="contact__icon" viewBox="0 0 24 24" aria-hidden="true"><circle cx="12" cy="12" r="12" fill="#fff"/><path d="M8.2 5.6c.5-.3 1.1-.2 1.4.3l1.3 2.3c.3.5.1 1.1-.3 1.4l-.9.6c.6 1.6 1.8 2.9 3.4 3.6l.6-.9c.3-.5.9-.6 1.4-.3l2.3 1.3c.5.3.6.9.3 1.4l-.9 1.5c-.4.6-1.1.9-1.8.7C10.6 16.4 7.6 13.4 6.4 9.2c-.2-.7.1-1.4.7-1.8z" fill="#141414"/></svg>
      <span>817-555-0187</span>
    </div>

    <div class="contact contact--fax">
      <svg class="contact__icon" viewBox="0 0 24 24" aria-hidden="true"><circle cx="12" cy="12" r="12" fill="#fff"/><rect x="8.5" y="5.5" width="7" height="4" fill="#141414"/><rect x="6" y="10" width="12" height="7.5" rx="1" fill="#141414"/><rect x="8.5" y="13.5" width="7" height="1.2" fill="#fff"/></svg>
      <span>817-555-0163</span>
    </div>
  </section>
</main>
</body>
</html>
```